Business Card Design

Contact Information for Business Card

A vertical business card request- a medium & light gray with silverpine tree logo (logo is attached)

Please use Trebuchet font -- if possible- can we use two different color gray? (See pictures attached below)
Info on the front should be the Silverpine tree logo - on the top of the card, followed by the info ...
Card to read: " " indicated what should be on the card --
Name: " Carla Merrow "
Title : "Partner "
" Office: 202.555.0147 "
" Mobile: 202.555.0183 "

Backside of the card - solid medium color gray color w/ address and small message centered in the card - Trebuchet font
to read:

" 718 B North Larkmoor Avenue, NE "
" Washington, DC 20019 "

Then below address to read:
" Fundraising | Event Planning | Political Consulting "

```html
<!DOCTYPE html>
<html lang="en">
<head>
<meta charset="utf-8">
<title>Silverpine Strategies – Business Cards</title>
<link href="https://fonts.googleapis.com/css2?family=Fira+Sans:wght@300;400&display=swap" rel="stylesheet">
<style>
  :root {
    --backdrop: #e9e7e3;
    --card-light: #8c8c8c;
    --card-dark: #58595b;
    --text-white: #ffffff;
    --text-soft: #d4d4d4;
    --name-gray: #a7a8aa;
    --branch-tone: #6a6b6d;
    --shadow: rgba(0, 0, 0, 0.28);
  }
  * { margin: 0; padding: 0; box-sizing: border-box; }
  html, body {
    width: 1200px;
    height: 843px;
    overflow: hidden;
    background: var(--backdrop);
    font-family: "Trebuchet MS", "Fira Sans", sans-serif;
  }
  .stage { position: relative; width: 1200px; height: 843px; }

  .card {
    position: absolute;
    top: 110px;
    width: 356px;
    height: 623px;
    overflow: hidden;
    box-shadow: 0 10px 24px var(--shadow);
  }

  /* Address side */
  .card--address {
    left: 640px;
    background: var(--card-light);
  }
  .brand {
    position: absolute;
    left: 0;
    right: 0;
    top: 70px;
    text-align: center;
    color: var(--text-soft);
    font-weight: 300;
    line-height: 1;
  }
  .brand__mark {
    display: block;
    width: 96px;
    height: 96px;
    margin: 0 auto 26px;
    border-radius: 50%;
    background: var(--text-white);
  }
  .brand__name {
    display: block;
    font-size: 32px;
    letter-spacing: 3px;
  }
  .brand__tag {
    display: block;
    margin-top: 8px;
    font-size: 12px;
    letter-spacing: 3px;
    color: var(--text-white);
  }
  .address {
    position: absolute;
    left: 0;
    right: 0;
    top: 360px;
    text-align: center;
    color: var(--text-white);
    font-size: 15px;
    line-height: 1.5;
  }
  .address__services { margin-top: 18px; }

  /* Contact side */
  .card--contact {
    left: 204px;
    background: var(--card-dark);
  }
  .branch-art {
    position: absolute;
    left: 0;
    right: 0;
    top: 0;
    height: 360px;
    background: linear-gradient(160deg, var(--card-dark) 10%, var(--branch-tone) 55%, var(--card-dark) 95%);
  }
  .contact {
    position: absolute;
    left: 40px;
    bottom: 44px;
    color: var(--text-white);
    font-size: 16px;
    line-height: 1.45;
  }
  .contact__name {
    color: var(--name-gray);
    font-size: 25px;
    line-height: 1.2;
  }
  .contact__title { margin-bottom: 12px; }
</style>
</head>
<body>
  <main class="stage">
    <section class="card card--contact">
      <div class="branch-art" role="img" aria-label="Faint tree branch decoration"></div>
      <div class="contact">
        <p class="contact__name">Carla Merrow</p>
        <p class="contact__title">Partner</p>
        <p>Office: 202.555.0147</p>
        <p>Mobile: 202.555.0183</p>
        <p>carla@silverpinellc.com</p>
      </div>
    </section>

    <section class="card card--address">
      <div class="brand">
        <span class="brand__mark"></span>
        <span class="brand__name">SILVERPINE</span>
        <span class="brand__tag">STRATEGIES</span>
      </div>
      <div class="address">
        <p>718 B North Larkmoor Avenue, NE</p>
        <p>Washington, DC 20019</p>
        <p class="address__services">Fundraising | Event Planning</p>
        <p>Political Consulting</p>
      </div>
    </section>
  </main>
</body>
</html>
```